VELUNDORA Multistep design - needs to match our existing design.

We have a multistep form(7 pages) we need the design for (rest of the website is done).
The multistep form is a vital part of the website, as it is the main service - so the form design should fit into the rest of the site.
Please take a look at the attached file - all about colors, fonts etc. is included in the file.

Target Market(s)

People looking for an interior architect in Denmark

Industry/Entity Type

Interior Design

Number of Pages Required

1 page

Requirements
Nice to have
• It's attached in the pdf file

```html
<!DOCTYPE html>
<html lang="da">
<head>
<meta charset="utf-8">
<title>VELUNDORA – Konceptet</title>
<link href="https://fonts.googleapis.com/css2?family=Source+Sans+3:wght@400;600;700&family=Raleway:wght@300;400;700&family=Roboto:wght@500&display=swap" rel="stylesheet">
<style>
:root{
  --ink:#ffffff;
  --hero-dark:#1c2228;
  --hero-mid:#4a4e52;
  --hero-light:#8a8886;
  --navy:#324350;
  --footer:#334452;
  --field-top:#ffffff;
  --field-bottom:#cfcfcf;
  --tab:#e4e4e4;
  --tab-text:#3d4a55;
  --chat:#2c3e4c;
  --badge:#e8194a;
}
*{margin:0;padding:0;box-sizing:border-box}
html,body{width:1200px;height:1019px;overflow:hidden}
body{position:relative;font-family:"Source Sans 3",sans-serif;color:var(--ink);background:var(--footer)}
.hero{position:absolute;left:0;top:0;width:1200px;height:681px;
  background:radial-gradient(ellipse at 60% 45%,var(--hero-light) 0%,var(--hero-mid) 40%,var(--hero-dark) 100%)}
.hero::after{content:"";position:absolute;inset:0;background:rgba(20,28,36,.35)}
.abs{position:absolute;z-index:1}
.brand{left:60px;top:26px;font-size:32px;font-weight:400;letter-spacing:.5px}
.nav a{position:absolute;top:33px;height:42px;line-height:42px;font-size:21px;color:var(--ink);text-decoration:none;white-space:nowrap}
.nav .active{left:490px;width:119px;background:#fff;color:#111;text-align:center}
.tabs{left:414px;top:147px;width:282px;height:36px;border-bottom:2px solid var(--tab)}
.tab{position:absolute;top:0;height:35px;line-height:37px;font-size:27px}
.tab-private{left:0;width:121px;background:var(--tab);color:var(--tab-text);text-align:center;border-radius:6px 6px 0 0}
.tab-business{left:146px}
.label{font-size:21px;text-align:center;width:400px;white-space:nowrap}
.field{height:39px;width:354px;background:linear-gradient(var(--field-top),var(--field-bottom))}
.check{font-size:21px;display:flex;align-items:center;gap:10px}
.continue{left:380px;top:577px;width:349px;height:49px;background:var(--navy);border-radius:4px;
  font-size:31px;font-weight:700;text-align:center;line-height:49px;letter-spacing:.5px}
.footer-brand{left:0;width:1200px;top:772px;text-align:center;font-family:Raleway,sans-serif;font-weight:300;font-size:36px}
.foot{font-family:Raleway,sans-serif;font-size:11px;line-height:21.5px;text-align:center}
.foot b{font-weight:700}
.chat-bubble{left:961px;top:950px;width:151px;height:39px;background:var(--chat);border-radius:20px;
  font-family:Roboto,sans-serif;font-weight:500;font-size:13px;line-height:39px;text-align:center}
.chat-btn{left:1125px;top:943px;width:52px;height:52px;background:var(--chat);border-radius:50%}
.badge{left:1165px;top:939px;width:17px;height:17px;background:var(--badge);border-radius:50%;
  font-size:10px;font-weight:700;text-align:center;line-height:17px;z-index:2}
</style>
</head>
<body>
<div class="hero" role="img" aria-label="Dimmed photo of an architect drawing on plans at a desk with a ruler and rolled drawings"></div>

<div class="abs brand">VELUNDORA</div>
<nav class="nav">
  <a class="abs active">Konceptet</a>
  <a class="abs" style="left:642px">Privat</a>
  <a class="abs" style="left:738px">Erhverv</a>
  <a class="abs" style="left:852px">Arkitekt</a>
  <a class="abs" style="left:967px">Om VELUNDORA</a>
</nav>

<div class="abs tabs">
  <span class="tab tab-private">PRIVATE</span>
  <span class="tab tab-business">BUSINESS</span>
</div>

<div class="abs label" style="left:149px;top:219px">First Name</div>
<div class="abs field" style="left:181px;top:253px"></div>
<div class="abs label" style="left:550px;top:219px">Last Name</div>
<div class="abs field" style="left:574px;top:253px"></div>

<div class="abs label" style="left:142px;top:301px">Address</div>
<div class="abs field" style="left:181px;top:336px"></div>
<div class="abs label" style="left:545px;top:299px">Email</div>
<div class="abs field" style="left:574px;top:336px"></div>

<div class="abs label" style="left:142px;top:384px">Phone</div>
<div class="abs field" style="left:181px;top:415px"></div>
<div class="abs label" style="left:545px;top:382px">Post code</div>
<div class="abs field" style="left:574px;top:415px"></div>

<div class="abs label" style="left:142px;top:465px">Minimum Budget</div>
<div class="abs field" style="left:178px;top:501px"></div>
<div class="abs label" style="left:556px;top:465px">Is the case about a house or an apartment</div>

<div class="abs check" style="left:620px;top:508px">
  <svg width="22" height="22" viewBox="0 0 22 22"><path d="M16 3H3v16h16v-7" fill="none" stroke="#fff" stroke-width="2.2"/><path d="M6 10l4 4 9-10" fill="none" stroke="#fff" stroke-width="2.4"/></svg>House
</div>
<div class="abs check" style="left:731px;top:508px">
  <svg width="22" height="22" viewBox="0 0 22 22"><path d="M16 3H3v16h16v-7" fill="none" stroke="#fff" stroke-width="2.2"/><path d="M6 10l4 4 9-10" fill="none" stroke="#fff" stroke-width="2.4"/></svg>Appartment
</div>

<div class="abs continue">CONTINUE</div>

<div class="abs footer-brand">VELUNDORA</div>
<div class="abs foot" style="left:124px;top:817px;width:300px">
  VELUNDORA er din portal, hvor du kan indhente to gratis<br>matches på arkitekter til din indretningsopgave. Du<br>udfylder alle oplysninger om din opgave, og vores<br>database udregner det bedste match til dig – helt<br>uforpligtende og gratis.<br>Kom igang lige <b>her</b>
</div>
<div class="abs foot" style="left:500px;top:838px;width:200px">
  Solbakkevej 14<br>8230, Åbyhøj<br><br>+45 12 34 56 78<br>kontakt@velundora.dk
</div>
<div class="abs foot" style="left:766px;top:817px;width:320px">
  <b>Er du arkitekt?</b><br>Ønsker du at blive en del af VELUNDORA, så klik <b>her</b> og bliv<br>nemt en del af vores arkitektdatabase.
</div>

<div class="abs chat-bubble">What's your question?</div>
<div class="abs chat-btn">
  <svg width="52" height="52" viewBox="0 0 52 52"><path d="M16 17h20v13H24l-5 4v-4h-3z" fill="none" stroke="#fff" stroke-width="2.6" stroke-linejoin="round"/><path d="M21 23h10" stroke="#fff" stroke-width="2.4"/></svg>
</div>
<div class="abs badge">1</div>
</body>
</html>
```